Website for cloud software, Coded

We would like a website designed for an invoicing software used in the cloud. It is a new product based on a PC-loaded software that we have sold for 10 years, refer www.billquarry.example
Winner will need to code the page in HTML with everything a functional website needs.

Target Market(s)

small business owners

Industry/Entity Type

Software

Requirements
Must have
• We would need:
Homepage (description of product)
Features (to be able to put screenshots)
Pricing & Sign-up
Contact & About

Page 1 - Home page
introduction to billquarry!Sky - the next step up from PC-based billquarry (sold since 1999). Same product, but use from anywhere with any mobile device.

Page 2 - Features
provides screen shots of this extensive program and must have room for plenty of text to accompany the images. Refer www.tumbled-slate.example/features for scope. Looking for quick-load page with innovative presentation of the features

Page 3 - Pricing
includes Pricing, Sign-up, Contact and Log-in (for existing users)
Pricing has single-month price, and concession rates for signing up a year in advance
Sign-up is a link to an external page where people can try the program free for 14 days.

Page 4 Contact & About
Contact is a box for people to write to us with questions (sent to info@billquarry.example)
Log-in (for existing users) is a link to an external page where existing users can log on to their program (they will also get a shortcut from us that makes sign-on quicker).
A brief history of our Company and billquarry! software

We would like a crisp modern look for the website.
Emphasise access to software with any mobile device and from anywhere that has internet access.
Nice to have
• It should be editable in Frontpage. Pictures of stylised cloud is acceptable.
Should not have
• Website style:
we don't have any style in mind, except we DON'T want black or dark background. Fast loading, so avoid use of extensive flash stuff.

```html
<!DOCTYPE html>
<html lang="en">
<head>
<meta charset="utf-8">
<title>billquarry! – Invoicing and Billing Software for Business</title>
<link href="https://fonts.googleapis.com/css2?family=Archivo+Narrow:wght@400;600;700&display=swap" rel="stylesheet">
<style>
:root{
  --blue:#1b4f7c;
  --blue-dark:#0f3553;
  --heading:#1f5f93;
  --green:#7ea82f;
  --green-dark:#5f8a1c;
  --orange:#f7a20b;
  --orange-dark:#e48700;
  --page:#f6f6f6;
  --card:#ececec;
  --text:#555;
  --muted:#8a8a8a;
  --footer:#1f1f1f;
  --white:#fff;
}
*{box-sizing:border-box;margin:0;padding:0}
html,body{width:817px;height:1200px;overflow:hidden}
body{font-family:"Archivo Narrow",Arial,sans-serif;background:var(--page);color:var(--text);position:relative}
a{color:inherit;text-decoration:none}
.abs{position:absolute}

/* header */
.site-header{position:absolute;left:0;top:0;width:817px;height:117px;background:var(--white);border-top:3px solid var(--blue)}
.call-tab{left:583px;top:-3px;width:164px;height:36px;background:var(--blue);color:var(--white);font-size:12px;display:flex;align-items:center;justify-content:center;gap:6px;border-radius:0 0 4px 4px}
.brand{left:69px;top:34px;display:flex;align-items:center;gap:8px}
.brand-mark{width:22px;height:22px;border-radius:50%;background:var(--orange)}
.brand-name{font-size:32px;font-weight:700;color:var(--blue)}
.main-nav{left:311px;top:72px;display:flex;gap:22px;font-size:14px;color:#666}
.main-nav a{display:flex;align-items:center;gap:6px;padding-bottom:4px}
.main-nav a.current{color:var(--blue);border-bottom:2px solid var(--blue)}
.search{left:628px;top:69px;width:113px;height:24px;border:1px solid #ddd;border-radius:3px;font-size:11px;color:#aaa;padding:5px 10px;display:flex;justify-content:space-between;align-items:center}

/* hero */
.hero{left:0;top:117px;width:817px;height:374px;background:radial-gradient(ellipse at 40% 30%,#8fc6e6 0%,#3f86b3 30%,#1b4566 65%,#0c2234 100%)}
.hero-panel{left:57px;top:253px;width:436px;height:167px;background:rgba(20,30,40,.55);padding:16px 12px}
.hero-title{font-size:53px;color:var(--white);line-height:1}
.hero-sub{font-size:19px;color:var(--white);margin-top:6px}
.btn{display:inline-block;background:linear-gradient(var(--orange),var(--orange-dark));color:var(--white);text-align:center}
.hero-btn{margin-top:14px;width:156px;height:31px;line-height:31px;font-size:20px}

/* plans */
.plan{top:517px;width:226px;height:216px;background:var(--card);border-radius:6px;box-shadow:0 3px 3px rgba(0,0,0,.25);text-align:center}
.plan-head{height:40px;background:linear-gradient(#93bf3e,var(--green-dark));border-radius:6px 6px 0 0;color:var(--white);font-size:20px;display:flex;align-items:center;gap:12px;padding-left:18px}
.plan-desc{font-size:12px;line-height:16px;margin:26px auto 0;width:180px;height:32px}
.plan-order{font-size:20px;color:#444;margin-top:6px}
.plan-trial{font-size:12px;margin-top:10px}
.plan-btn{margin-top:16px;width:124px;height:27px;line-height:27px;font-size:14px}

/* services */
.section-title{font-size:27px;color:var(--heading)}
.service{top:819px;width:137px;height:90px;overflow:hidden}
.service-caption{position:absolute;left:0;bottom:0;width:100%;height:22px;background:rgba(30,30,30,.75);color:var(--white);font-size:10px;text-align:center;line-height:22px}
.services-text{left:72px;top:930px;width:430px;font-size:10.5px;line-height:17px;color:var(--muted)}

/* testimonials */
.quote{left:523px;width:230px;display:flex;gap:11px}
.quote-photo{width:48px;height:48px;flex:none;background:linear-gradient(#b08a70,#5a3e30)}
.quote-text{font-size:11px;line-height:17px;color:var(--muted)}
.quote-name{color:var(--orange-dark);margin-top:5px}
.divider{left:523px;top:900px;width:200px;height:1px;background:#ddd}

/* partners */
.partners{left:200px;top:1027px;width:430px;display:flex;justify-content:space-between;align-items:center}
.partner{display:flex;align-items:center;gap:7px;font-size:28px;font-weight:700}
.partner i{display:block;width:20px;height:20px}

/* footer */
.site-footer{left:0;top:1091px;width:817px;height:109px;background:var(--footer);color:var(--white)}
.foot-nav{left:60px;top:12px;display:flex;gap:5px;font-size:12px}
.foot-nav a{background:#3a3a3a;border-radius:3px;padding:3px 6px}
.share{left:62px;top:51px;display:flex;align-items:center;gap:6px;font-size:13px}
.share-label{margin-right:6px}
.share i{display:block;width:18px;height:18px;border-radius:3px}
.social{left:368px;top:14px;font-size:10px;line-height:20px}
.social a{display:flex;align-items:center;gap:7px}
.social span{display:block;width:13px;height:13px;border-radius:50%;background:var(--white)}
.subscribe{left:565px;top:10px;display:flex;height:26px}
.subscribe-field{width:125px;background:var(--white);color:#aaa;font-size:9px;padding:7px 6px;border-radius:2px 0 0 2px}
.subscribe-btn{width:64px;background:var(--orange);font-size:13px;text-align:center;line-height:26px}
.copyright{left:62px;top:88px;font-size:9px}
</style>
</head>
<body>

<header class="site-header">
  <a class="call-tab abs" href="#">
    <svg width="12" height="12" viewBox="0 0 24 24"><path fill="#fff" d="M6.6 10.8a15 15 0 0 0 6.6 6.6l2.2-2.2c.3-.3.7-.4 1-.2 1.1.4 2.3.6 3.6.6.6 0 1 .4 1 1V20c0 .6-.4 1-1 1A17 17 0 0 1 3 4c0-.6.4-1 1-1h3.5c.6 0 1 .4 1 1 0 1.3.2 2.5.6 3.6.1.3 0 .7-.2 1z"/></svg>
    CALL US: (5550) 410 772
  </a>
  <a class="brand abs" href="#"><span class="brand-mark"></span><span class="brand-name">billquarry!</span></a>
  <nav class="main-nav abs">
    <a class="current" href="#"><svg width="15" height="13" viewBox="0 0 16 14"><path fill="currentColor" d="M8 0 0 7h2v7h4V9h4v5h4V7h2z"/></svg>Home</a>
    <a href="#"><svg width="17" height="13" viewBox="0 0 18 14"><circle cx="6" cy="4" r="3" fill="currentColor"/><circle cx="13" cy="4" r="3" fill="currentColor"/><path d="M0 14c0-4 3-6 6-6s6 2 6 6zM10 9c1-1 2-1 3-1 3 0 5 2 5 6h-5" fill="currentColor"/></svg>About</a>
    <a href="#"><svg width="14" height="14" viewBox="0 0 14 14"><circle cx="7" cy="7" r="5" fill="none" stroke="currentColor" stroke-width="3" stroke-dasharray="2.5 1.5"/><circle cx="7" cy="7" r="2" fill="currentColor"/></svg>Features</a>
    <a href="#"><svg width="16" height="12" viewBox="0 0 16 12"><path fill="currentColor" d="M0 0h7v12H0zM9 0h7v12H9z"/></svg>Contact</a>
  </nav>
  <div class="search abs">keyword
    <svg width="11" height="11" viewBox="0 0 12 12"><circle cx="7" cy="5" r="4" fill="none" stroke="#1b4f7c" stroke-width="2"/><path d="M4 8 0 12" stroke="#1b4f7c" stroke-width="2"/></svg>
  </div>
</header>

<section class="hero abs" role="img" aria-label="Photo of a finger touching glowing blue app tiles"></section>
<div class="hero-panel abs">
  <h1 class="hero-title">billquarry!</h1>
  <p class="hero-sub">Invoicing and Billing Software for Business</p>
  <a class="btn hero-btn" href="#">Take a Tour</a>
</div>

<article class="plan abs" style="left:60px">
  <div class="plan-head"><svg width="26" height="26" viewBox="0 0 26 26"><circle cx="10" cy="10" r="7" fill="none" stroke="#fff" stroke-width="3"/><path d="M15 15l9 9" stroke="#fff" stroke-width="4"/></svg>billquarry! Lite</div>
  <p class="plan-desc">it's lighter, simple as and it costs a whole lot less.</p>
  <p class="plan-order">Order now</p>
  <p class="plan-trial">Download free 30-day trial</p>
  <a class="btn plan-btn" href="#">Order Now!</a>
</article>
<article class="plan abs" style="left:297px">
  <div class="plan-head"><svg width="26" height="26" viewBox="0 0 26 26"><path d="M3 3l20 20M23 3 3 23" stroke="#fff" stroke-width="4"/></svg>billquarry! Time+</div>
  <p class="plan-desc">Time-billing has just become easier...</p>
  <p class="plan-order">Order now</p>
  <p class="plan-trial">Download free 30-day trial</p>
  <a class="btn plan-btn" href="#">Order Now!</a>
</article>
<article class="plan abs" style="left:531px">
  <div class="plan-head"><svg width="26" height="26" viewBox="0 0 26 26"><path d="M2 2v22h22" fill="none" stroke="#fff" stroke-width="2"/><path d="M5 20l5-7 4 4 8-11" fill="none" stroke="#fff" stroke-width="2"/></svg>billquarry! Pro</div>
  <p class="plan-desc">the complete invoice and billing software.</p>
  <p class="plan-order">Order now</p>
  <p class="plan-trial">Download free 30-day trial</p>
  <a class="btn plan-btn" href="#">Order Now</a>
</article>

<h2 class="section-title abs" style="left:72px;top:768px">billquarry Services</h2>
<div class="service abs" style="left:72px" role="img" aria-label="Illustration of a cloud over a city skyline"><div style="width:100%;height:100%;background:linear-gradient(#8ed0ea,#3a8fb8)"></div><span class="service-caption">Fantastic features</span></div>
<div class="service abs" style="left:216px" role="img" aria-label="Photo of a rising financial chart"><div style="width:100%;height:100%;background:linear-gradient(#2a3f9a,#0b1450)"></div><span class="service-caption">Growing&nbsp; Businesses</span></div>
<div class="service abs" style="left:360px" role="img" aria-label="Photo of people working at computers"><div style="width:100%;height:100%;background:linear-gradient(#7a6a5e,#3a2e28)"></div><span class="service-caption">Create Invoices</span></div>
<p class="services-text abs">billquarry! is an easy to learn and affordable invoice application which works smarter than similar invoice and billing software and keeps you totally informed about your business with many custom reports. Use billquarry! for invoicing and generating invoices on the go or to run your entire business.</p>

<h2 class="section-title abs" style="left:521px;top:768px">What they say</h2>
<div class="quote abs" style="top:819px">
  <div class="quote-photo" role="img" aria-label="Portrait photo of a customer"></div>
  <div class="quote-text">Sed a orci nec dolor molestie aliquam volutpat et lacus. Sed vulputate arcu imperdiet.<p class="quote-name">Della MARSH - Manger</p></div>
</div>
<div class="divider abs"></div>
<div class="quote abs" style="top:914px">
  <div class="quote-photo" role="img" aria-label="Portrait photo of a customer"></div>
  <div class="quote-text">Aenean quis mollis nulla. Donec mollis mi eu lectus mollis sagittis. Integer fermentum facilisis.<p class="quote-name">Irene COLBY - Manger</p></div>
</div>

<div class="partners abs">
  <span class="partner" style="color:#e41b23"><i style="background:#e41b23"></i>Norvane</span>
  <span class="partner" style="color:#222">Quillstead</span>
  <span class="partner" style="color:#d52b1e"><i style="background:#d52b1e;border-radius:50%"></i>TALMOUR</span>
</div>

<footer class="site-footer abs">
  <nav class="foot-nav abs"><a href="#">Home</a><a href="#">About</a><a href="#">Solutions</a><a href="#">Blog</a><a href="#">Contact us</a></nav>
  <div class="share abs"><span class="share-label">Share this:</span>
    <i style="background:#3b5998"></i><i style="background:#555"></i><i style="background:#ccc"></i><i style="background:#2a9fd6"></i><i style="background:#4aa3df"></i><i style="background:#888"></i><i style="background:#c4302b"></i><i style="background:#f68b1f"></i>
  </div>
  <div class="social abs">
    <a href="#"><span></span>Friendwall</a>
    <a href="#"><span></span>Chirper</a>
    <a href="#"><span></span>Workconnect</a>
  </div>
  <div class="subscribe abs"><span class="subscribe-field">you@mailbox.example</span><a class="subscribe-btn" href="#">Subscribe</a></div>
  <p class="copyright abs">billquarry! 2013 Copyright.All rights Reserved!</p>
</footer>

</body>
</html>
```